Pet Care company needs label design for new product. Eco-friendly, amazing results helping anima...

We need a label designed for a new eco-friendly pet care product. The product is highly effective, non-medicated, 100% safe to use on all animals. The product is an aqueous solution that uses a low PH to create an environment unfavorable for the grow of bacteria and fungus. Target market is horses, dogs and cats. Most common uses will be for rain rot, hot spots, ear infections and wound care. **Bottle is green with a white sprayer. Here is the specifications for the label; Trim size: 8.375 x 4.25 (w x h), please keep all critical art at least 1/8 inch away from trim line.Bleeds: Include 1/8 inch bleeds, and keep all critical art at least 1/8 inch away from trim line.

Target Market(s)

Pet owners; horses, dogs and cats

Industry/Entity Type

Pet Care

Font styles to use
Serif

Colors

Designer to choose colors to be used in the design.

Requirements
Must have
• Images of horses, dogs, cats. Geared to the eco-friendly nature of the product. It is not "organic" but I want that kind of look.
Nice to have
• Product information uploaded.
Should not have
• I do not want the product to look cartoonish. It is a highly effective treatment for animals with skin infections. I want people to feel by looking at the product it works.

```html
<!DOCTYPE html>
<html lang="en">
<head>
<meta charset="utf-8">
<title>Meadow's Mend – Eco-Friendly Pet Care Label</title>
<link href="https://fonts.googleapis.com/css2?family=Montserrat:wght@400;600;700&family=Fjalla+One&display=swap" rel="stylesheet">
<style>
  :root {
    --leaf: #6abf45;
    --slate: #557a7a;
    --ink: #4a4f54;
    --paper: #ffffff;
    --canvas: #f3f4f3;
    --photo-a: #e9ecea;
    --photo-b: #c9b79a;
  }
  * { box-sizing: border-box; margin: 0; padding: 0; }
  html, body { width: 1200px; height: 1120px; overflow: hidden; }
  body { background: var(--canvas); font-family: "Montserrat", sans-serif; color: var(--ink); position: relative; }

  .label {
    position: absolute; top: 180px; width: 540px; height: 760px;
    background: var(--paper); box-shadow: 0 2px 10px rgba(0,0,0,.08); overflow: hidden;
  }
  .label--back { left: 40px; }
  .label--front { left: 620px; }

  .edge-band { position: absolute; left: 0; right: 0; height: 18px; background: var(--leaf); }
  .edge-band--top { top: 0; }
  .edge-band--bottom { bottom: 0; }
  .edge-band::after { content: ""; position: absolute; left: 0; right: 0; height: 2px; background: var(--leaf); }
  .edge-band--top::after { bottom: -6px; }
  .edge-band--bottom::after { top: -6px; }

  .animal-photo {
    position: absolute;
    background: radial-gradient(ellipse at 50% 45%, var(--photo-a) 0%, #dcdfdc 45%, var(--photo-b) 80%, rgba(255,255,255,0) 100%);
    border-radius: 40% 40% 30% 30%;
  }

  .brand-name {
    font-family: "Montserrat", sans-serif; font-weight: 600; color: var(--slate);
    line-height: 1.08; letter-spacing: 0;
  }
  .brand-mark { display: inline-block; background: var(--slate); }

  /* back label */
  .label--back .animal-photo { left: 34px; top: 60px; width: 180px; height: 240px; }
  .label--back .brand { position: absolute; left: 224px; top: 84px; width: 290px; }
  .label--back .brand-mark { width: 14px; height: 14px; margin-bottom: 12px; }
  .label--back .brand-name { font-size: 50px; }
  .tagline-box {
    position: absolute; left: 224px; top: 228px; width: 288px; padding: 9px 0;
    background: var(--leaf); color: #fff; font-weight: 600; font-size: 15px; text-align: center; letter-spacing: .3px;
  }

  .info-panel { position: absolute; left: 40px; top: 330px; width: 460px; height: 345px; border: 2px solid var(--leaf); }
  .panel-head { background: var(--leaf); color: #fff; font-weight: 600; font-size: 12px; padding: 5px 10px; }
  .directions { list-style: none; padding: 8px 12px 4px; }
  .directions li { font-size: 10px; margin-bottom: 13px; padding-left: 16px; position: relative; }
  .directions li::before { content: ""; position: absolute; left: 0; top: 3px; width: 6px; height: 6px; border-radius: 50%; background: var(--ink); }
  .how-text { font-size: 10px; line-height: 2; padding: 10px 12px 8px; }
  .claims-bar { display: flex; justify-content: space-between; align-items: center; background: var(--leaf); color: #fff; font-weight: 600; font-size: 11.5px; padding: 5px 8px; }
  .claim { display: flex; align-items: center; gap: 6px; }
  .claim svg { width: 15px; height: 15px; }
  .fine-row { display: flex; justify-content: space-between; padding: 6px 10px 0; font-size: 9.5px; }
  .active { text-align: right; line-height: 1.8; }
  .active b { color: var(--leaf); font-weight: 600; font-style: italic; }
  .distributor { margin-top: 14px; }
  .foot-row { position: absolute; left: 0; right: 0; bottom: 0; display: flex; justify-content: space-between; align-items: flex-end; }
  .use-tag {
    background: var(--leaf); color: #fff; font-weight: 600; font-size: 11px; padding: 6px 34px 6px 10px;
    clip-path: polygon(0 0, 100% 0, 90% 100%, 0 100%);
  }
  .vet-note { font-size: 7.5px; text-align: right; padding: 0 8px 4px; line-height: 1.3; }

  /* front label */
  .label--front .brand { position: absolute; left: 0; right: 0; top: 52px; text-align: center; }
  .label--front .brand-mark { width: 20px; height: 20px; margin-bottom: 16px; }
  .label--front .brand-name { font-size: 84px; }
  .tagline-band {
    position: absolute; left: 0; right: 0; top: 282px; height: 60px; background: var(--leaf);
    color: #fff; font-weight: 600; font-size: 24px; display: flex; align-items: center; justify-content: center; letter-spacing: .3px;
    border-top: 3px solid #fff; outline: 2px solid var(--leaf);
  }
  .label--front .animal-photo { left: 24px; top: 362px; width: 290px; height: 370px; }
  .uses { position: absolute; left: 340px; top: 378px; list-style: none; font-family: "Fjalla One", sans-serif; color: var(--slate); font-size: 19px; }
  .uses li { margin-bottom: 6px; padding-left: 20px; position: relative; }
  .uses li::before { content: ""; position: absolute; left: 0; top: 10px; width: 8px; height: 8px; border-radius: 50%; background: var(--leaf); }
  .uses-rule { position: absolute; left: 340px; top: 522px; width: 40px; height: 3px; background: var(--leaf); }
  .front-copy { position: absolute; left: 340px; top: 550px; width: 180px; font-size: 12.5px; line-height: 1.3; color: var(--slate); }
  .volume-badge {
    position: absolute; left: 350px; top: 658px; width: 64px; height: 64px; border-radius: 50%;
    border: 3px solid var(--leaf); box-shadow: inset 0 0 0 3px #fff, inset 0 0 0 32px var(--leaf);
    color: #fff; font-family: "Fjalla One", sans-serif; font-size: 11px; display: flex; flex-direction: column; align-items: center; justify-content: center; line-height: 1.2;
  }
</style>
</head>
<body>

<section class="label label--back">
  <div class="edge-band edge-band--top"></div>
  <div class="animal-photo" role="img" aria-label="Photo of a white horse standing behind a ginger cat and a beagle"></div>
  <div class="brand">
    <span class="brand-mark"></span>
    <div class="brand-name">Meadow's<br>Mend</div>
  </div>
  <div class="tagline-box">ECO-FRIENDLY PET CARE</div>

  <div class="info-panel">
    <div class="panel-head">DIRECTIONS</div>
    <ul class="directions">
      <li>Clean affected; removing dirt, debris, removing scabs is not necessary.</li>
      <li>Spray MEADOW'S MEND over affected area. No need for gloves.</li>
      <li>Repeat 2-3 times daily until affected area is healed.</li>
    </ul>
    <div class="panel-head">HOW DOES THIS WORK?</div>
    <p class="how-text">MEADOW'S MEND is a natural, eco-friendly, toxic and chemical free solution. MEADOW'S MEND lowers the PH of the affected area creating an environment unfavorable for bacterial and fungal growth.</p>
    <div class="claims-bar">
      <span class="claim">
        <svg viewBox="0 0 16 16"><rect x="1" y="2" width="14" height="12" fill="none" stroke="#fff" stroke-width="1.5"/><path d="M3 12 L13 4" stroke="#fff" stroke-width="1.5"/></svg>
        NON-CORROSIVE TO THE SKIN
      </span>
      <span class="claim">
        <svg viewBox="0 0 16 16"><path d="M8 1 L14 3 V8 C14 11.5 11 14 8 15 C5 14 2 11.5 2 8 V3 Z" fill="#fff"/><path d="M5 8 L7.3 10.3 L11 6" fill="none" stroke="#6abf45" stroke-width="1.6"/></svg>
        SAFE FOR ALL ANIMALS
      </span>
    </div>
    <div class="fine-row">
      <span class="distributor">Distributed by MEADOW'S MEND, LLC.</span>
      <span class="active"><b>Active Ingredient:</b><br>Electrolyzed 2.8% Hydronium</span>
    </div>
    <div class="foot-row">
      <span class="use-tag">Typical use only. Not for internal use.</span>
      <span class="vet-note">For serious, recurring infections<br>consult with a veterinarian</span>
    </div>
  </div>
  <div class="edge-band edge-band--bottom"></div>
</section>

<section class="label label--front">
  <div class="edge-band edge-band--top"></div>
  <div class="brand">
    <span class="brand-mark"></span>
    <div class="brand-name">Meadow's<br>Mend</div>
  </div>
  <div class="tagline-band">ECO-FRIENDLY PET CARE</div>
  <div class="animal-photo" role="img" aria-label="Photo of a white horse standing behind a ginger cat and a beagle"></div>
  <ul class="uses">
    <li>Rain Rot</li>
    <li>Hot Spots</li>
    <li>Surface wounds</li>
    <li>Ringworm and More!</li>
  </ul>
  <div class="uses-rule"></div>
  <p class="front-copy">None medicated, safe, effective aid providing a healing environment for recovery from fungal and bacterial infections.</p>
  <div class="volume-badge"><span>16 FL OZ</span><span>473 ml</span></div>
  <div class="edge-band edge-band--bottom"></div>
</section>

</body>
</html>
```